TRU PEAK POWER.

I'd like my business logo.
contact name: Desmond Halvik
phone:0438275160
email: info@trupeakpower.net.au
website: www.trupeakpower.net.au

services:
solar
battery storage
LED lighting
energy saving solutions
general electrical
I'd like the design to look professional

Target Market(s)

Everyone

Industry/Entity Type

Business

Contact Information for Business Card

as described above

Requirements
Must have
• Id like the colours and the design to work well with my logo.

```html
<!DOCTYPE html>
<html lang="en">
<head>
<meta charset="utf-8">
<title>Tru Peak Power – Business Card</title>
<link href="https://fonts.googleapis.com/css2?family=Open+Sans:wght@400;600;700;800&display=swap" rel="stylesheet">
<style>
  :root {
    --backdrop: #ecebe7;
    --leaf-green: #95c83a;
    --brand-green: #4fa83d;
    --sun-orange: #f5a21b;
    --ink-grey: #4a4a4a;
    --paper: #ffffff;
    --rule: #8a8a8a;
  }
  * { margin: 0; padding: 0; box-sizing: border-box; }
  html, body {
    width: 1200px; height: 900px; overflow: hidden;
    background: var(--backdrop);
    font-family: "Open Sans", Arial, sans-serif;
  }
  .canvas { position: relative; width: 1200px; height: 900px; }

  .card {
    position: absolute;
    width: 560px; height: 342px;
    border-radius: 4px;
    box-shadow: 0 10px 28px rgba(0,0,0,0.18);
    overflow: hidden;
  }

  /* Front */
  .card-front {
    left: 80px; top: 110px;
    background: var(--leaf-green);
  }
  .front-wordmark {
    position: absolute; left: 0; right: 0; top: 134px;
    text-align: center;
    color: var(--paper);
    font-weight: 800; font-size: 52px; letter-spacing: 1px;
  }

  /* Back */
  .card-back {
    left: 560px; top: 440px;
    background: var(--paper);
  }
  .holder-name {
    position: absolute; right: 34px; top: 26px;
    color: var(--sun-orange);
    font-weight: 700; font-size: 16px; letter-spacing: 0.5px;
    text-transform: uppercase;
  }
  .back-logo {
    position: absolute; left: 60px; top: 80px;
    display: flex; align-items: center; gap: 14px;
  }
  .logo-dot {
    width: 44px; height: 44px; border-radius: 50%;
    background: var(--sun-orange);
  }
  .back-wordmark {
    color: var(--brand-green);
    font-weight: 800; font-size: 38px; letter-spacing: 0.5px;
  }
  .contact-list {
    position: absolute; right: 34px; top: 158px;
    list-style: none; text-align: right;
    color: var(--ink-grey); font-size: 13px; line-height: 20px;
  }
  .contact-list li { display: flex; justify-content: flex-end; align-items: center; gap: 6px; }
  .contact-list svg { width: 11px; height: 11px; fill: var(--sun-orange); }
  .services {
    position: absolute; left: 34px; bottom: 34px;
  }
  .services-title {
    color: var(--sun-orange);
    font-weight: 600; font-size: 19px; margin-bottom: 6px;
  }
  .services-list {
    list-style: none; display: flex;
    color: var(--ink-grey); font-size: 15px;
  }
  .services-list li + li::before {
    content: "|"; color: var(--rule); margin: 0 8px;
  }
</style>
</head>
<body>
<main class="canvas">

  <section class="card card-front" aria-label="Card front">
    <p class="front-wordmark">TRU PEAK POWER</p>
  </section>

  <section class="card card-back" aria-label="Card back">
    <p class="holder-name">Desmond Halvik</p>

    <div class="back-logo">
      <span class="logo-dot" aria-hidden="true"></span>
      <span class="back-wordmark">TRU PEAK POWER</span>
    </div>

    <ul class="contact-list">
      <li>0438275160
        <svg viewBox="0 0 24 24" aria-hidden="true"><path d="M6.6 10.8a15.1 15.1 0 0 0 6.6 6.6l2.2-2.2a1 1 0 0 1 1-.25 11.4 11.4 0 0 0 3.6.57 1 1 0 0 1 1 1V20a1 1 0 0 1-1 1A17 17 0 0 1 3 4a1 1 0 0 1 1-1h3.5a1 1 0 0 1 1 1c0 1.25.2 2.45.57 3.6a1 1 0 0 1-.25 1z"/></svg>
      </li>
      <li>info@trupeakpower.net.au
        <svg viewBox="0 0 24 24" aria-hidden="true"><path d="M2 5h20v14H2zm2 2v.5l8 5 8-5V7z"/></svg>
      </li>
      <li>www.trupeakpower.net.au
        <svg viewBox="0 0 24 24" aria-hidden="true"><path d="M3 17.2V21h3.8L17.8 10l-3.8-3.8zM20.7 7a1 1 0 0 0 0-1.4l-2.3-2.3a1 1 0 0 0-1.4 0l-1.8 1.8 3.8 3.8z"/></svg>
      </li>
    </ul>

    <div class="services">
      <p class="services-title">What I do</p>
      <ul class="services-list">
        <li>Solar</li>
        <li>Battery Storage</li>
        <li>LED Lighting</li>
        <li>Energy Saving Solutions</li>
      </ul>
    </div>
  </section>

</main>
</body>
</html>
```